Falcon guarding business card

Looking for a business card for my security company

Target Market(s)

Security

Industry/Entity Type

Security

Contact Information for Business Card

Name - Dale Hutchins. Title - General manager - direct 318 642.9053 website www. falconguardingservices.example email - dale@ falconguardingservices.example

Requirements
Must have
• Logo attached

```html
<!DOCTYPE html>
<html lang="en">
<head>
<meta charset="utf-8">
<title>Falcon guarding — business card</title>
<link href="https://fonts.googleapis.com/css2?family=Exo+2:wght@400;600;700&display=swap" rel="stylesheet">
<style>
  :root {
    --stage: #c4c4c4;
    --card: #2a2a2a;
    --gold: #d4a53a;
    --gold-light: #f0d27a;
    --white: #ececec;
    --gloss: #5a5a5a;
    --rule: #cfcfcf;
  }
  * { box-sizing: border-box; margin: 0; padding: 0; }
  html, body { width: 1200px; height: 800px; overflow: hidden; }
  body {
    background: var(--stage);
    font-family: "Exo 2", sans-serif;
    display: flex;
    align-items: center;
    justify-content: center;
    gap: 50px;
  }
  .card {
    position: relative;
    width: 540px;
    height: 309px;
    background: var(--card);
    overflow: hidden;
  }
  .card--front::after {
    content: "";
    position: absolute;
    left: 0; right: 0; bottom: 0;
    height: 12px;
    background: linear-gradient(90deg, var(--gold), var(--gold-light), var(--gold));
  }
  .card--back { border-bottom: 3px solid var(--gold); }

  .brand-name {
    font-weight: 700;
    text-transform: uppercase;
    letter-spacing: 1px;
    line-height: 1;
  }
  .front-brand {
    position: absolute;
    left: 34px;
    top: 128px;
    width: 200px;
    display: flex;
    align-items: center;
    gap: 10px;
    color: var(--gold);
    font-size: 25px;
  }
  .brand-mark {
    width: 14px; height: 14px;
    border-radius: 50%;
    background: var(--gold);
    flex: none;
  }
  .divider {
    position: absolute;
    left: 258px;
    top: 100px;
    width: 1px;
    height: 96px;
    background: var(--rule);
  }
  .contact {
    position: absolute;
    left: 282px;
    top: 92px;
    color: var(--white);
  }
  .contact__name {
    color: var(--gold);
    font-weight: 700;
    font-size: 22px;
    text-transform: uppercase;
    letter-spacing: 0.5px;
  }
  .contact__title {
    font-size: 14px;
    margin-top: 2px;
    margin-bottom: 16px;
  }
  .contact__list { list-style: none; font-size: 13px; line-height: 1.55; }
  .contact__list li { display: flex; align-items: center; gap: 8px; }
  .contact__list svg { width: 11px; height: 11px; fill: var(--gold); flex: none; }

  .back-brand {
    position: absolute;
    inset: 0;
    display: flex;
    align-items: center;
    justify-content: center;
    color: var(--gloss);
    font-size: 46px;
  }
</style>
</head>
<body>
  <section class="card card--front">
    <div class="front-brand">
      <span class="brand-mark"></span>
      <span class="brand-name">Falcon guarding</span>
    </div>
    <div class="divider"></div>
    <div class="contact">
      <p class="contact__name">Dale Hutchins</p>
      <p class="contact__title">General manager</p>
      <ul class="contact__list">
        <li>
          <svg viewBox="0 0 24 24" aria-hidden="true"><path d="M6.6 10.8a15.1 15.1 0 0 0 6.6 6.6l2.2-2.2a1 1 0 0 1 1-.25 11.4 11.4 0 0 0 3.6.57 1 1 0 0 1 1 1V20a1 1 0 0 1-1 1A17 17 0 0 1 3 4a1 1 0 0 1 1-1h3.5a1 1 0 0 1 1 1c0 1.25.2 2.45.57 3.57a1 1 0 0 1-.25 1z"/></svg>
          318 642.9053
        </li>
        <li>
          <svg viewBox="0 0 24 24" aria-hidden="true"><path d="M2 5h20v14H2z M2 5l10 8 10-8" /></svg>
          dale@ falconguardingservices.example
        </li>
        <li>
          <svg viewBox="0 0 24 24" aria-hidden="true"><circle cx="12" cy="12" r="10"/></svg>
          falconguardingservices.example
        </li>
      </ul>
    </div>
  </section>

  <section class="card card--back">
    <div class="back-brand">
      <span class="brand-name">Falcon guarding</span>
    </div>
  </section>
</body>
</html>
```